I need a business card for my original fine art pieces

I would like a business card design including a logo design for a new business in the art world. I am based in the Hunter Valley NSW Australia. I am a contemporary figurative, encaustic and wildlife artist. I would like to be able to upload my email and mobile number to this as well. This design should be one that I can incorporate into banners and flyers etc. Id like to incorporate one of my own images or partial image into the background or somewhere below. My initials are KR and I would like these used as a logo type. I would like the use of some colour and it to be bright and catchy. The final design should communicate artwork custom made and commissions available.

Overview: Original Fine Artworks for sale, online, art galleries etc, Custom made to order and by commission.

Target market is world wide audience and corporate world

My figurative work is painted using acrylics in a lot of natural ochre colours that reflect the Australian Outback, on canvas, linen, paper or board: My encaustic work is created in a contemporary abstract style using a blow torch and a made with a medium of 100% pure bees wax, Damar resin, mixed media and coloured pigments, applied to Birch board. My wildlife are created using coloured pencil and mixed media on a variety of paper types or board.

```html
<!DOCTYPE html>
<html lang="en">
<head>
<meta charset="utf-8">
<title>Kara Reid — Business Card</title>
<link rel="stylesheet" href="https://fonts.googleapis.com/css2?family=Cinzel:wght@600&family=Arimo:wght@400&family=Open+Sans:wght@400;600&display=swap">
<style>
  :root {
    --stage-top: #2a2a2a;
    --stage-bottom: #050505;
    --brand-orange: #ff4500;
    --brand-orange-text: #f2490f;
    --card-white: #ffffff;
    --ink: #111111;
    --body-text: #444444;
    --rule: #9a9a9a;
  }
  * { margin: 0; padding: 0; box-sizing: border-box; }
  html, body { width: 1200px; height: 900px; overflow: hidden; }
  body {
    position: relative;
    background: linear-gradient(180deg, var(--stage-top) 0%, #1a1a1a 45%, var(--stage-bottom) 100%);
  }
  .card {
    position: absolute;
    top: 306px;
    width: 440px;
    height: 271px;
    border-radius: 12px;
    box-shadow: 0 4px 14px rgba(0,0,0,0.5);
  }
  .card--front { left: 149px; background: var(--card-white); }
  .card--back { left: 608px; background: var(--brand-orange); }

  .wordmark {
    position: absolute;
    left: 0; right: 0;
    text-align: center;
    font-family: "Cinzel", serif;
    font-weight: 600;
    line-height: 1;
  }
  .tagline {
    position: absolute;
    left: 0; right: 0;
    text-align: center;
    font-family: "Arimo", sans-serif;
    line-height: 1;
    text-transform: uppercase;
    white-space: nowrap;
  }
  .card--front .wordmark { top: 54px; font-size: 40px; color: var(--brand-orange-text); letter-spacing: 1.5px; }
  .card--front .tagline { top: 93px; font-size: 17.5px; letter-spacing: 3.6px; color: var(--ink); }

  .address {
    position: absolute;
    left: 26px; top: 160px;
    font-family: "Open Sans", sans-serif;
    font-size: 11.5px;
    line-height: 16px;
    color: var(--body-text);
  }
  .person {
    position: absolute;
    right: 22px; top: 176px;
    text-align: right;
    font-family: "Open Sans", sans-serif;
  }
  .person__name { font-size: 14px; font-weight: 600; color: var(--brand-orange-text); line-height: 18px; }
  .person__role { font-size: 11.5px; color: var(--body-text); line-height: 16px; margin-top: 5px; }
  .rule {
    position: absolute;
    left: 26px; right: 22px; top: 198px;
    height: 1px; background: var(--rule);
  }
  .contacts {
    position: absolute;
    left: 26px; top: 203px;
    list-style: none;
    font-family: "Open Sans", sans-serif;
    font-size: 11.5px;
    line-height: 16px;
    color: var(--body-text);
  }
  .contacts li { display: flex; align-items: center; gap: 7px; }
  .contacts svg { width: 9px; height: 9px; fill: var(--brand-orange); flex: none; }

  .brand-circle {
    position: absolute;
    left: 170px; top: 62px;
    width: 102px; height: 102px;
    border: 3px solid var(--card-white);
    border-radius: 50%;
  }
  .card--back .wordmark { top: 167px; font-size: 32px; color: var(--card-white); letter-spacing: 1.5px; }
  .card--back .tagline { top: 199px; font-size: 14px; letter-spacing: 2.9px; color: var(--card-white); }
</style>
</head>
<body>
  <section class="card card--front">
    <div class="wordmark">Kara Reid</div>
    <div class="tagline">Original Fine Artworks</div>

    <p class="address">12345, Address Goes Here<br>Country Name, 123456.</p>
    <div class="person">
      <div class="person__name">Daniel Hayes</div>
      <div class="person__role">Managing Director</div>
    </div>
    <div class="rule"></div>

    <ul class="contacts">
      <li>
        <svg viewBox="0 0 10 10" aria-hidden="true"><path d="M2 0.5 L3.6 2.6 L2.8 3.6 C3.4 5 4.9 6.6 6.4 7.2 L7.4 6.4 L9.5 8 L8.6 9.5 C4.8 9.2 0.8 5.2 0.5 1.4 Z"/></svg>
        044-123 456 789
      </li>
      <li>
        <svg viewBox="0 0 10 10" aria-hidden="true"><path d="M0.5 2 H9.5 V8 H0.5 Z M1 2.5 L5 5.5 L9 2.5" /></svg>
        info@webname.com
      </li>
      <li>
        <svg viewBox="0 0 10 10" aria-hidden="true"><circle cx="5" cy="5" r="4.5"/></svg>
        www.websitename.com
      </li>
    </ul>
  </section>

  <section class="card card--back">
    <div class="brand-circle" aria-hidden="true"></div>
    <div class="wordmark">Kara Reid</div>
    <div class="tagline">Original Fine Artworks</div>
  </section>
</body>
</html>
```